Business Goals Posters for display within company office and factory.

We have three (3) high level business goals we want to display in the office and factory areas of the business.

1. Under the heading of "QUALITY"
"We will have pride and ownership of every product and service delivered to our customers."

2. Under the heading of "PRODUCTIVITY"
"We will put the customer's expectations first and ensure our team is empowered to do so."

3. Under the heading of "SAFETY"
"We will shift our culture to ensure safety is our first thought on every job."

We would like a matching set of posters with these three headings and statements with a background suitable for display in a business environment. The posters will be displayed in sizes from A4 and A2.
The company's logo is Red and Black (see attachment) .
We make Electric and Hydraulic power packs for industrial market.
our website will give you an idea of what we do www.tarnwickdrives.com.au

Industry/Entity Type

Power Generation

Colors

Designer to choose colors to be used in the design.

Requirements
Must have
• The posters must use the exact text provided and have the headings listed.
• the three posters must have a common theme. they can be different in back ground but when side by side must look like a set.
• Be suitable for display as A4 and as A2.
Nice to have
• The text needs the be the star, the background needs to draw attention to the poster and the text with out over powering it,
Should not have
• not have photo's of generators or equipment as backgrounds

```html
<!DOCTYPE html>
<html lang="en">
<head>
<meta charset="utf-8">
<title>Tarnwick Drives – Business Goals</title>
<link rel="stylesheet" href="https://fonts.googleapis.com/css2?family=Oswald:wght@500;600&family=Open+Sans:wght@400&display=swap">
<style>
  :root {
    --brand-red: #ee1f26;
    --ink: #000000;
    --paper: #ffffff;
  }
  * { margin: 0; padding: 0; box-sizing: border-box; }
  html, body { width: 1200px; height: 848px; overflow: hidden; background: var(--paper); }
  .poster { position: relative; width: 1200px; height: 848px; background: var(--paper); overflow: hidden; }
  .bands { position: absolute; inset: 0; }
  .goal { position: absolute; left: 0; width: 800px; }
  .goal__icon { position: absolute; left: 70px; }
  .goal__title {
    position: absolute; left: 229px;
    font-family: "Oswald", sans-serif; font-weight: 500;
    font-size: 60px; line-height: 1; letter-spacing: -1.5px;
  }
  .goal__text {
    position: absolute; left: 229px; width: 560px;
    font-family: "Open Sans", sans-serif; font-weight: 400;
    font-size: 23.5px; line-height: 28px;
  }
  .goal--quality, .goal--safety { color: var(--paper); }
  .goal--productivity { color: var(--ink); }
  .goal--quality { top: 0; }
  .goal--quality .goal__title { top: 50px; }
  .goal--quality .goal__text { top: 126px; }
  .goal--quality .goal__icon { top: 78px; }
  .goal--productivity { top: 0; }
  .goal--productivity .goal__title { top: 342px; }
  .goal--productivity .goal__text { top: 426px; }
  .goal--productivity .goal__icon { top: 362px; }
  .goal--safety { top: 0; }
  .goal--safety .goal__title { top: 638px; }
  .goal--safety .goal__text { top: 724px; }
  .goal--safety .goal__icon { top: 664px; }
  .brand {
    position: absolute; left: 905px; top: 108px;
    display: flex; align-items: center; gap: 12px;
    font-family: "Oswald", sans-serif; font-weight: 600;
    font-size: 40px; line-height: 1; color: var(--ink); letter-spacing: 0.5px;
  }
  .brand__square { width: 26px; height: 26px; background: var(--brand-red); }
</style>
</head>
<body>
<main class="poster">
  <svg class="bands" width="1200" height="848" viewBox="0 0 1200 848" aria-hidden="true">
    <polygon points="0,0 722,0 866,264 0,264" fill="var(--brand-red)"/>
    <polygon points="670,279 1200,279 1200,558 866,558" fill="var(--ink)"/>
    <polygon points="0,572 906,572 1056,848 0,848" fill="var(--brand-red)"/>
  </svg>

  <div class="brand"><span class="brand__square"></span>Tarnwick Drives</div>

  <section class="goal goal--quality">
    <svg class="goal__icon" width="100" height="100" viewBox="0 0 100 100" aria-hidden="true">
      <g fill="none" stroke="var(--paper)" stroke-width="6" stroke-linejoin="round" stroke-linecap="round">
        <rect x="5" y="38" width="18" height="56" rx="3"/>
        <path d="M23 44 L40 36 L50 14 Q52 4 60 8 Q66 12 64 24 L60 38 L88 38 Q98 40 96 50 Q94 56 88 57 Q96 60 94 68 Q92 74 86 74 Q92 78 88 85 Q86 90 78 90 L40 92 L23 88"/>
      </g>
      <circle cx="14" cy="82" r="3" fill="var(--paper)"/>
    </svg>
    <h2 class="goal__title">QUALITY</h2>
    <p class="goal__text">We will have pride and owership of every product and service delivered to our customers.</p>
  </section>

  <section class="goal goal--productivity">
    <svg class="goal__icon" width="110" height="110" viewBox="0 0 110 110" aria-hidden="true">
      <g fill="none" stroke="var(--ink)">
        <circle cx="38" cy="71" r="33" stroke-width="9" stroke-dasharray="8 6"/>
        <circle cx="38" cy="71" r="26" stroke-width="6"/>
        <circle cx="38" cy="71" r="19" stroke-width="3"/>
        <circle cx="38" cy="71" r="7" stroke-width="4"/>
        <circle cx="82" cy="23" r="22" stroke-width="7" stroke-dasharray="6 5"/>
        <circle cx="82" cy="23" r="17" stroke-width="5"/>
        <circle cx="82" cy="23" r="11" stroke-width="3"/>
        <circle cx="82" cy="23" r="5" stroke-width="3"/>
      </g>
    </svg>
    <h2 class="goal__title">PRODUCTIVITY</h2>
    <p class="goal__text">We will put the customer's expectations first and ensure our team is empowered to do so.</p>
  </section>

  <section class="goal goal--safety">
    <svg class="goal__icon" width="92" height="92" viewBox="0 0 92 92" aria-hidden="true">
      <path d="M46 2 Q66 12 90 10 L90 40 Q88 70 46 88 Q4 70 2 40 L2 10 Q26 12 46 2 Z" fill="var(--paper)"/>
      <line x1="2" y1="14" x2="72" y2="74" stroke="var(--brand-red)" stroke-width="4"/>
    </svg>
    <h2 class="goal__title">SAFETY</h2>
    <p class="goal__text">We will shift our culture to ensure safety is our first thought on every job.</p>
  </section>
</main>
</body>
</html>
```